Design for a newly formed Real Estate Management Company - Velloran Management

Background
Velloran Management is a Real Estate Company that manages properties for a small family business. I'd like to showcase the properties that I've acquired and turned around so they're performing well. This website will be a way for me to promote my business.

Different Sections
This website will help promote the work that I've been doing so it should include an About Us page. There should also be a page that goes through the different properties that we've managed and turned around. It would be great to have a design that allows me to visually show the different buildings that may be in various areas in a creative fashion. Finally, I need a section for a blog where I write about certain things prospective property owners should know about.

Design
http://www.dunquest7.example/ is a good example of the type of design I'm looking for. For the about us page, I'd like it to be able to show a portrait photo and a section to give some information about the person. I will be adding more people to the team so if there's a way to easily add photos and descriptions of new members, that would be great.

Target Market(s)

Third Party Real Estate Servicers (i.e. Insurance, Mortgage Brokers, Brokers)
Investors who are thinking to invest with us
Tenants who want to see how well we manage properties

Industry/Entity Type

Real Estate

Number of Pages Required

3 page

Requirements
Must have
• Integration of the logo into the design of the website would be a must. I'd like the design to flow together well and not be pages kind of stitched together. There should also be a way for me to easily add properties to the list. I should be able to monitor the people that join the website and obtain a login. It would be great to be able to edit and add things to the design so things aren't hardcoded.
Nice to have
• Allow tenants to write reviews of their experience at the property. Should not be anonymous, they would need to log in so at least their first name will show. Blog should also have log in so they may comment on the posts.

```html
<!DOCTYPE html>
<html lang="en">
<head>
<meta charset="utf-8">
<title>Velloran Management</title>
<link href="https://fonts.googleapis.com/css2?family=Open+Sans:wght@400;600&family=Raleway:wght@400;500;600&display=swap" rel="stylesheet">
<style>
:root{
  --blue:#2d76b3;
  --blue-dark:#2a5f9c;
  --navy:#2b3a7c;
  --footer-bottom:#2a6aa3;
  --ink:#333;
  --muted:#777;
  --pale:#e7f1f8;
  --white:#fff;
  --line:#ddd;
}
*{box-sizing:border-box;margin:0;padding:0}
html,body{width:702px;height:1200px;overflow:hidden;background:var(--white)}
body{position:relative;font-family:"Raleway",sans-serif;color:var(--ink)}
.abs{position:absolute}
/* header */
.brand{left:58px;top:26px;display:flex;align-items:center;gap:8px}
.brand-mark{width:22px;height:22px;background:var(--navy)}
.brand-name{font-family:"Open Sans",sans-serif;font-weight:600;font-size:17px;color:var(--blue-dark);letter-spacing:.5px}
.call{left:527px;top:22px;font-family:"Open Sans",sans-serif}
.call b{display:block;font-size:10px;font-weight:600;color:var(--blue-dark)}
.call span{font-size:9px;color:var(--muted)}
.call-icon{left:622px;top:27px}
.nav{left:58px;top:74px;width:586px;height:27px;background:var(--blue);display:flex}
.nav a{flex:1 1 auto;color:var(--white);font-size:7.5px;font-weight:500;text-decoration:none;display:flex;align-items:center;justify-content:center;border-right:1px solid rgba(255,255,255,.15);letter-spacing:.2px}
.nav a.active{background:var(--navy);flex:0 0 71px}
/* hero */
.hero{left:0;top:101px;width:702px;height:251px;background:linear-gradient(180deg,#e9eef3 0%,#d7dee6 55%,#b9c5cf 100%)}
.hero-arrow{top:217px;width:27px;height:27px;border-radius:50%;background:rgba(120,120,120,.35)}
.caption{left:293px;top:258px;width:351px;height:51px;background:rgba(70,70,70,.75);color:var(--white);font-family:"Open Sans",sans-serif;font-size:10px;line-height:15px;text-align:right;padding:9px 17px}
.find-tab{left:58px;top:331px;width:90px;height:21px;background:var(--navy);color:var(--white);font-size:7px;font-weight:600;display:flex;align-items:center;justify-content:center}
.search{left:0;top:352px;width:702px;height:62px;background:var(--blue)}
.field{top:369px;color:var(--white);font-size:7px}
.select{position:absolute;top:12px;left:0;height:19px;background:var(--white);border-radius:2px;color:#999;font-size:6.5px;padding:6px 5px}
.select i{position:absolute;right:3px;top:3px;width:13px;height:13px;background:var(--blue-dark)}
.select i:after{content:"";position:absolute;left:4px;top:5px;border:3px solid transparent;border-top:4px solid var(--white)}
.submit{left:604px;top:379px;width:40px;height:19px;background:var(--navy);color:var(--white);font-size:7px;font-weight:600;border-radius:2px;display:flex;align-items:center;justify-content:center}
/* welcome */
.section-title{width:702px;left:0;text-align:center;font-family:"Open Sans",sans-serif;font-size:12.5px;color:#222}
.intro{left:70px;top:470px;width:562px;font-size:7px;line-height:10.5px;color:var(--muted);text-align:center}
.read-more{left:300px;top:512px;width:100px;height:19px;border:1px solid var(--blue);border-radius:2px;color:var(--blue);font-size:7px;font-weight:600;display:flex;align-items:center;justify-content:center}
.divider{left:58px;top:554px;width:586px;border-top:1px dotted #ccc}
/* property cards */
.card{top:605px;width:131px;height:169px;border:1px solid #e4e4e4;background:var(--white)}
.card-photo{position:absolute;left:0;top:0;width:129px;height:87px}
.price{position:absolute;left:0;top:0;width:70px;height:20px;background:var(--blue);color:var(--white);font-family:"Open Sans",sans-serif;font-size:9px;padding:4px 0 0 14px}
.card h3{position:absolute;left:10px;top:100px;font-size:6.8px;font-weight:500;color:#222}
.card p{position:absolute;left:10px;top:112px;width:112px;font-size:6.5px;line-height:10px;color:#999}
.card a{position:absolute;left:10px;top:146px;font-size:6.5px;color:#444;text-decoration:none}
.pager{top:789px}
/* testimonials */
.testimonials{left:0;top:834px;width:702px;height:188px;background:var(--pale)}
.quote-box{left:60px;top:904px;width:581px;height:69px;background:var(--white);border-radius:2px}
.quote-text{left:100px;top:917px;width:500px;font-size:6.5px;line-height:10.5px;color:#888;text-align:center}
.quote-by{left:0;top:950px;width:702px;font-size:6.5px;color:#555;text-align:center}
.quote-by span{color:var(--blue)}
.qmark{top:917px;font-family:"Open Sans",sans-serif;font-size:22px;font-weight:600;color:var(--blue);line-height:1}
.dot{top:988px;width:5px;height:5px;border-radius:50%;background:#333}
/* footer */
.footer{left:0;top:1022px;width:702px;height:143px;background:var(--blue)}
.foot-bottom{left:0;top:1165px;width:702px;height:35px;background:var(--footer-bottom)}
.fcol{top:1045px;color:var(--white)}
.fcol h4{font-size:7.5px;font-weight:600;margin-bottom:6px;letter-spacing:.2px}
.fcol p{font-size:6.3px;line-height:8.5px}
.fcol ul{list-style:none;font-size:6.3px;line-height:11.5px}
.fcol li:before{content:"";display:inline-block;width:3px;height:3px;background:var(--white);border-radius:50%;margin:0 9px 1px 2px}
.contact-line{display:flex;align-items:center;gap:6px;font-size:6.3px;line-height:11px}
.input{width:115px;height:16px;background:rgba(255,255,255,.22);border:1px solid rgba(255,255,255,.3);font-size:6px;padding:4px 5px;color:var(--white);position:relative}
.fbtn{left:594px;top:1134px;width:45px;height:14px;background:var(--navy);color:var(--white);font-size:6.5px;font-weight:600;display:flex;align-items:center;justify-content:center}
.copy{left:55px;top:1178px;font-size:6px;color:var(--white)}
.social{top:1178px;width:8px;height:8px;border-radius:50%;background:var(--white)}
</style>
</head>
<body>

<header>
  <div class="abs brand"><span class="brand-mark"></span><span class="brand-name">Velloran Management</span></div>
  <div class="abs call"><b>Call Us</b><span>+(21) 600 - 18 - 7042</span></div>
  <svg class="abs call-icon" width="22" height="22" viewBox="0 0 22 22" aria-hidden="true">
    <circle cx="11" cy="11" r="9.5" fill="none" stroke="#3a9ad6" stroke-width="1.6"/>
    <path d="M7.5 6.5c.6-.4 1.2-.3 1.5.3l.8 1.6c.2.4.1.8-.2 1.1l-.5.5c.5 1.1 1.4 2 2.5 2.5l.5-.5c.3-.3.7-.4 1.1-.2l1.6.8c.6.3.7.9.3 1.5-.8 1.1-2.1 1.3-3.3.7-2-1-3.6-2.6-4.6-4.6-.6-1.2-.4-2.5.3-3.7z" fill="#3a9ad6"/>
  </svg>
  <nav class="abs nav">
    <a class="active" href="#">HOME</a><a href="#">SERVICES</a><a href="#">ABOUT US</a><a href="#">WHO WE ARE</a><a href="#">GALLERY</a><a href="#">TESTIMONIALS</a><a href="#">CONTACT US</a>
  </nav>
</header>

<section>
  <div class="abs hero" role="img" aria-label="Photo of a couple standing in front of a large white two-storey house with columns"></div>
  <svg class="abs hero-arrow" style="left:17px" viewBox="0 0 27 27" aria-hidden="true"><path d="M15 9l-4 4.5 4 4.5" stroke="#fff" stroke-width="1.6" fill="none"/></svg>
  <svg class="abs hero-arrow" style="left:657px" viewBox="0 0 27 27" aria-hidden="true"><path d="M12 9l4 4.5-4 4.5" stroke="#fff" stroke-width="1.6" fill="none"/></svg>
  <div class="abs caption">Velloran Management is a Real Estate management Company that manages properties for a small family business</div>
  <div class="abs find-tab">FIND PROPERTY</div>
  <div class="abs search"></div>
  <div class="abs field" style="left:58px">Property type:<div class="select" style="width:81px">choose..<i></i></div></div>
  <div class="abs field" style="left:158px">Location:<div class="select" style="width:81px">choose..<i></i></div></div>
  <div class="abs field" style="left:257px">Price Range:<div class="select" style="width:61px">min price<i></i></div></div>
  <div class="abs field" style="left:328px"><span style="visibility:hidden">x</span><div class="select" style="width:61px">max price<i></i></div></div>
  <div class="abs field" style="left:408px">Bedrooms:<div class="select" style="width:81px">1<i></i></div></div>
  <div class="abs field" style="left:508px">Bathrooms:<div class="select" style="width:81px">1<i></i></div></div>
  <div class="abs submit">Submit</div>
</section>

<section>
  <h2 class="abs section-title" style="top:443px">Welcome To Our Site</h2>
  <p class="abs intro">Lorem ipsum dolor sit amet, consectetur adipiscing elit. Nunc rutrum et lorem eget cursus. Sed rutrum placerat ex, vitae lacinia nisl dignissim vitae. Integer ultrices, est pulvinar blandit aliquet, arcu orci volutpat est, id porttitor odio velit id nibh. Vivamus Vestibulum sodales, sapien sit amet vulputate aliquet, felis risus fringilla felis, ac vulputate dolor nulla fringilla ante. Vivamus sit amet ipsum pharetra, faucibus dui nec, tempor lorem.</p>
  <div class="abs read-more">Read More</div>
  <div class="abs divider"></div>
</section>

<section>
  <h2 class="abs section-title" style="top:570px">Latest Properties</h2>
  <article class="abs card" style="left:60px">
    <div class="card-photo" role="img" aria-label="Hand holding house keys with a small model house" style="background:linear-gradient(135deg,#f2f2f2,#d8d2cc)"></div>
    <div class="price">$320.000</div>
    <h3>Sed pretium ut est et laoreet.</h3>
    <p>Ut lacinia ante sit amet neque ultrices, vitae posuere quam..</p>
    <a href="#">&#9776; More Details..</a>
  </article>
  <article class="abs card" style="left:210px">
    <div class="card-photo" role="img" aria-label="Suburban house with a for sale sign on the lawn" style="background:linear-gradient(180deg,#c9d3c7,#6f8a55)"></div>
    <div class="price">$280.000</div>
    <h3>318 Linden Avenue, Maple Court</h3>
    <p>Vivamus et mi et erat auctor laoreet id vel ante. Ut placerat..</p>
    <a href="#">&#9776; More Details..</a>
  </article>
  <article class="abs card" style="left:360px">
    <div class="card-photo" role="img" aria-label="Modern glass office towers against a blue sky" style="background:linear-gradient(160deg,#cfe3f5,#3e7fc4)"></div>
    <div class="price">$355.000</div>
    <h3>Sed pretium ut est et laoreet.</h3>
    <p>Praesent urna erat, lobortis eget mauris nec, sagittis sodales..</p>
    <a href="#">&#9776; More Details..</a>
  </article>
  <article class="abs card" style="left:510px">
    <div class="card-photo" role="img" aria-label="Happy family outdoors in front of a house and green lawn" style="background:linear-gradient(180deg,#d6dccf,#7fa54e)"></div>
    <div class="price">$3.500/mo</div>
    <h3>Route 12, Fernhill, OR</h3>
    <p>Class aptent taciti sociosqu ad litora torquent per conubia..</p>
    <a href="#">&#9776; More Details..</a>
  </article>
  <svg class="abs pager" style="left:333px" width="15" height="15" viewBox="0 0 15 15" aria-hidden="true"><circle cx="7.5" cy="7.5" r="6.7" fill="none" stroke="#333"/><path d="M8.5 5l-2.5 2.5 2.5 2.5" stroke="#333" fill="none"/></svg>
  <svg class="abs pager" style="left:353px" width="15" height="15" viewBox="0 0 15 15" aria-hidden="true"><circle cx="7.5" cy="7.5" r="6.7" fill="none" stroke="#333"/><path d="M6.5 5l2.5 2.5-2.5 2.5" stroke="#333" fill="none"/></svg>
</section>

<section>
  <div class="abs testimonials"></div>
  <h2 class="abs section-title" style="top:868px">Clients Testimonials</h2>
  <div class="abs quote-box"></div>
  <span class="abs qmark" style="left:73px">&ldquo;</span>
  <span class="abs qmark" style="left:613px">&rdquo;</span>
  <p class="abs quote-text">Etiam in tincidunt arcu, at tempor magna. Maecenas ut odio nunc. Fusce aliquet sem et sollicitudin tincidunt.<br>Aliquam convallis vitae metus ut luctus. Nulla vestibulum consequat sem, nec molestie tellus consectetur nec. In molestie sapien a convallis egestas.</p>
  <p class="abs quote-by">- Mara Ellison, <span>Lorm ipsum</span></p>
  <span class="abs dot" style="left:338px;background:var(--blue)"></span>
  <span class="abs dot" style="left:348px"></span>
  <span class="abs dot" style="left:358px"></span>
</section>

<footer>
  <div class="abs footer"></div>
  <div class="abs fcol" style="left:55px;width:130px">
    <h4>WHO WE ARE</h4>
    <p>Lorem ipsum dolor sit amet, consectetur adipiscing elit. Nullam venenatis velit blandit est condimentum aliquet. Curabitur ut libero justo. Nulla ut ex facilisis, tincidunt quam vitae, iaculis orci. Nullam eu faucibus nibh.</p>
    <p style="margin:13px 0 0 94px">More &#8594;</p>
  </div>
  <div class="abs fcol" style="left:237px">
    <h4>USEFUL LINKS</h4>
    <ul><li>Home</li><li>About Us</li><li>Service</li><li>FAQ</li><li>Sitemap</li><li>Contact Us</li></ul>
  </div>
  <div class="abs fcol" style="left:355px;width:130px">
    <h4>GET IN TOUCH</h4>
    <p>Doloreiur quia commolu ptatemp dolupta orepreruun tibusam eumenis et consent accullignis dentibea</p>
    <div style="margin-top:6px">
      <div class="contact-line"><svg width="6" height="7" viewBox="0 0 6 8"><path d="M3 0a3 3 0 0 1 3 3c0 2-3 5-3 5S0 5 0 3a3 3 0 0 1 3-3z" fill="#fff"/></svg>17 Harbor Lane, Ashford, State 30519</div>
      <div class="contact-line"><svg width="6" height="7" viewBox="0 0 8 8"><path d="M1 0l2 2-1 1.2c.7 1.3 1.5 2.1 2.8 2.8L6 5l2 2-1 1C3.5 8 0 4.5 0 1z" fill="#fff"/></svg>(212) 55 - 610 - 2047</div>
      <div class="contact-line"><svg width="6" height="7" viewBox="0 0 8 6"><rect width="8" height="6" fill="#fff"/><path d="M0 0l4 3 4-3" stroke="#2d76b3" fill="none"/></svg>hello@velloran.example</div>
    </div>
  </div>
  <div class="abs fcol" style="left:523px;width:120px">
    <h4>CONTACT</h4>
    <p>Doloreiur quia commolu ptatemp dolupta orepreruun</p>
    <div class="input" style="margin-top:8px">Email</div>
    <div class="input" style="margin-top:5px">Contact For<svg style="position:absolute;right:5px;top:5px" width="6" height="4" viewBox="0 0 6 4"><path d="M0 0l3 3 3-3" stroke="#fff" fill="none"/></svg></div>
  </div>
  <div class="abs fbtn">CONTACT</div>
  <div class="abs foot-bottom"></div>
  <p class="abs copy">&copy; 2016 yoursite. All rights reserved.</p>
  <span class="abs social" style="left:583px"></span>
  <span class="abs social" style="left:598px"></span>
  <span class="abs social" style="left:614px"></span>
  <span class="abs social" style="left:633px"></span>
</footer>

</body>
</html>
```